KWI Business Card

Please create a creative design for a business card using the new theme from the Logo & website. This company's main focus is food manufacturing building construction. Please integrate the new logo attached.

Please use the following information for the demo card:

Korvel Walls, Inc.
Dana Whitcombe
dwhitcombe@korvelwalls.example
Cell: 312-555-0178
218 Larkmoor Ave
Halvern, IL 60418

See pictures and more information on the website.

www.korvelwalls.example

```html
<!DOCTYPE html>
<html lang="en">
<head>
<meta charset="utf-8">
<title>KWI Business Card</title>
<link href="https://fonts.googleapis.com/css2?family=Open+Sans:wght@400;700&display=swap" rel="stylesheet">
<style>
  :root {
    --backdrop: #d2d3ce;
    --card: #ffffff;
    --brand-blue: #1f72c6;
    --ink: #1c1c1c;
    --rule: #2a78c8;
  }
  * { box-sizing: border-box; margin: 0; padding: 0; }
  html, body {
    width: 1200px; height: 801px; overflow: hidden;
    background: var(--backdrop);
    font-family: "Open Sans", sans-serif;
  }
  .stage {
    width: 1200px; height: 801px;
    display: flex; align-items: center; justify-content: center; gap: 56px;
  }
  .card {
    width: 520px; height: 297px;
    background: var(--card);
    border-bottom: 4px solid var(--brand-blue);
    box-shadow: 0 6px 18px rgba(0,0,0,0.18);
    position: relative;
    overflow: hidden;
  }
  /* Info side */
  .card-front { display: flex; align-items: center; }
  .front-brand {
    width: 240px; height: 100%;
    display: flex; align-items: center; justify-content: center; gap: 10px;
  }
  .divider {
    width: 1.5px; height: 130px; background: var(--rule); flex: none;
  }
  .contact {
    padding-left: 26px;
    padding-right: 16px;
    color: var(--ink);
    font-size: 12px; line-height: 1.45;
  }
  .contact-name {
    color: var(--brand-blue);
    font-weight: 700; font-size: 22px; letter-spacing: 0.3px;
    text-transform: uppercase; line-height: 1.1;
    white-space: nowrap;
  }
  .contact-title { margin-bottom: 8px; }
  .contact-address { margin-bottom: 6px; }
  .contact-row { display: flex; align-items: center; gap: 8px; white-space: nowrap; }
  .contact-row svg { width: 12px; height: 12px; flex: none; }
  .web-accent { color: var(--brand-blue); }
  /* Brand name block */
  .brand-mark {
    width: 14px; height: 14px; background: var(--brand-blue); flex: none;
  }
  .brand-name {
    color: var(--brand-blue); font-weight: 700; font-size: 18px; white-space: nowrap;
  }
  /* Logo side */
  .card-back {
    display: flex; align-items: center; justify-content: center; gap: 14px;
  }
  .card-back .brand-mark { width: 22px; height: 22px; }
  .card-back .brand-name { font-size: 32px; }
</style>
</head>
<body>
<main class="stage">
  <section class="card card-front">
    <div class="front-brand">
      <span class="brand-mark"></span>
      <span class="brand-name">Korvel Walls, Inc.</span>
    </div>
    <div class="divider"></div>
    <div class="contact">
      <div class="contact-name">Dana Whitcombe</div>
      <div class="contact-title">Founder &amp; CEO</div>
      <div class="contact-address">218 Larkmoor Ave<br>Halvern, IL 60418</div>
      <div class="contact-row">
        <svg viewBox="0 0 12 12"><path d="M2.5 1h2l1 3-1.4 1a6.5 6.5 0 0 0 3 3l1-1.4 3 1v2a1 1 0 0 1-1 1A9.5 9.5 0 0 1 1.5 2a1 1 0 0 1 1-1z" fill="var(--brand-blue)"/></svg>
        <span>312-555-0178</span>
      </div>
      <div class="contact-row">
        <svg viewBox="0 0 12 12"><rect x="0.5" y="2" width="11" height="8" fill="var(--brand-blue)"/><path d="M0.5 2l5.5 4.5L11.5 2" stroke="#fff" stroke-width="1" fill="none"/></svg>
        <span>dwhitcombe@korvelwalls.example</span>
      </div>
      <div class="contact-row">
        <svg viewBox="0 0 12 12"><circle cx="6" cy="6" r="5.3" fill="var(--brand-blue)"/><path d="M0.7 6h10.6M6 0.7v10.6M2 3.5h8M2 8.5h8" stroke="#fff" stroke-width="0.7"/><ellipse cx="6" cy="6" rx="2.4" ry="5.3" stroke="#fff" stroke-width="0.7" fill="none"/></svg>
        <span>www.<span class="web-accent">korvelwalls</span>.example</span>
      </div>
    </div>
  </section>

  <section class="card card-back">
    <span class="brand-mark"></span>
    <span class="brand-name">Korvel Walls, Inc.</span>
  </section>
</main>
</body>
</html>
```